Web re-design project www.varvikworks.com

We need a corporate website for a startup company called Varvik Works. The company offers web-based worksite management system for big construction companies. In short, replacing annoying papers with iPads.
We need the site main page to provide basic overview of the company and then inner page layout for displaying news and detailed information about products.
Currently we have a site up at:
http://www.varvikworks.com/en/main
but as you can see the graphic design is a bit lacking in quality(implemented by a tech guy :)
We need you to pimp that web site design up!
There is possibility for more freelance work in the future related to our web products, slide show designs and printed marketing materials.
Our main product is PELMO. You can find a short presentation about what it does here:
http://www.varvikworks.com/en/pelmo
Here you can find packages of images and screenshots related to our company:
https://files.stashbin.example/u/7720419/varvik_images.zip
https://files.stashbin.example/u/7720419/varvikworks%20images2.zip
Product logo svg can be found here:
https://files.stashbin.example/u/7720419/PELMO-logo.svg
Your are not forced to use those images, but hopefully there will be something that is useful.
Hope to hear from you guys soon!
Cheers,
Aarni
Update:
We will be using PELMO logo as the company brand. I don't like our current Varvik Works company logo, so that doesn't need to be included in the site design.
Update 2:
I like website designs that are "light", elegant and pretty simplistic. One example is our product login page (screenshot included in files).
Update 3:
Sites from the same industry / type of products:
http://www.rakomesta.fi/
http://www.brellinsurvey.com/products/software/network-applications/gradelane-3d
http://www.quostar.com/construction/heavy-civil/software-solutions/Linked-Crewfield.aspx?dtID=overview&
Target Market(s)
Target audience for the website is companies in the construction sector, and possibly corporate investors
Industry/Entity Type
Graphic Design
Look and feel

```html
<!DOCTYPE html>
<html lang="en">
<head>
<meta charset="utf-8">
<title>PELMO – Products</title>
<link rel="stylesheet" href="https://fonts.googleapis.com/css2?family=Montserrat:wght@400;500;600;700&family=Noto+Serif:ital@1&display=swap">
<style>
  :root {
    --band-blue: #3f5499;
    --nav-active: #3a58a0;
    --text-dark: #333333;
    --text-nav: #3c3c3c;
    --link-blue: #3f67c4;
    --heading-red: #e0101c;
    --rule-grey: #d2d2d2;
    --page-bg: #f3f3f3;
    --footer-top: #0a76c4;
    --footer-bottom: #05569c;
    --footer-text: #dce9f6;
    --copyright-bg: #efefef;
    --card-edge: #dedede;
  }
  * { box-sizing: border-box; margin: 0; padding: 0; }
  html, body { width: 1123px; height: 1200px; overflow: hidden; }
  body {
    position: relative;
    background: var(--page-bg);
    font-family: "Montserrat", sans-serif;
    color: var(--text-dark);
  }
  .top-band { position: absolute; left: 0; top: 0; width: 1123px; height: 447px; background: var(--band-blue); }
  .page {
    position: absolute; left: 37px; top: 15px; width: 1050px; height: 945px;
    background: #fff; border-radius: 8px 8px 0 0;
    box-shadow: 0 0 6px rgba(0,0,0,.25);
  }
  .brand {
    position: absolute; left: 21px; top: 40px;
    display: flex; align-items: center; gap: 14px;
    font-size: 52px; font-weight: 500; letter-spacing: 2px; color: #1b1b1b;
  }
  .brand-mark { width: 40px; height: 40px; border-radius: 50%; background: #1b1b1b; }
  .lang {
    position: absolute; left: 873px; top: 18px; width: 85px; height: 28px;
    background: #ececec; border-radius: 3px; font-size: 14px; color: #555;
    padding: 5px 0 0 11px;
  }
  .lang::after {
    content: ""; position: absolute; right: 9px; top: 12px;
    border: 5px solid transparent; border-top-color: #999;
  }
  .top-social { position: absolute; top: 18px; width: 27px; height: 27px; border-radius: 3px; }
  .nav { position: absolute; top: 75px; right: 21px; display: flex; gap: 6px; }
  .nav a {
    display: block; padding: 9px 10px; border-radius: 5px;
    font-size: 15.5px; font-weight: 500; text-decoration: none; color: var(--text-nav);
    margin-left: 9px;
  }
  .nav a.active { background: var(--nav-active); color: #fff; }
  .header-rule { position: absolute; left: 21px; top: 122px; width: 1008px; height: 3px; background: var(--rule-grey); }
  .hero {
    position: absolute; left: 21px; top: 141px; width: 1008px; height: 316px; border-radius: 6px;
    background: linear-gradient(90deg, #c9a23a 0%, #5f7a3e 35%, #6d8a4b 55%, #3f6fb5 78%, #d9b23a 100%);
  }
  .section-title {
    position: absolute; left: 21px; top: 487px;
    font-size: 34px; font-weight: 600; color: var(--heading-red);
  }
  .product-card {
    position: absolute; top: 548px; width: 483px; height: 182px;
    border: 1px solid var(--card-edge); border-radius: 6px;
    background: linear-gradient(#ffffff, #e9e9e9);
    box-shadow: inset 0 0 0 3px #fff;
  }
  .product-card.left { left: 20px; }
  .product-card.right { left: 547px; width: 481px; }
  .product-name {
    position: absolute; left: 25px; top: 22px;
    display: flex; align-items: center; gap: 12px;
    font-size: 46px; font-weight: 500; letter-spacing: 2px; color: #1b1b1b;
  }
  .product-name .dot { width: 34px; height: 34px; border-radius: 50%; background: #1b1b1b; }
  .product-name.small { font-size: 24px; top: 40px; color: #2a8ee0; letter-spacing: 1px; }
  .product-caption {
    position: absolute; left: 25px; top: 113px; width: 270px;
    font-size: 14.5px; font-weight: 600; line-height: 17px; color: var(--link-blue);
  }
  .chevron { position: absolute; right: 30px; top: 56px; }
  .footer {
    position: absolute; left: 0; top: 960px; width: 1123px; height: 197px;
    background: linear-gradient(var(--footer-top), var(--footer-bottom));
    color: #fff;
  }
  .footer-label { position: absolute; font-size: 14.5px; font-weight: 700; letter-spacing: .5px; }
  .footer-big { position: absolute; font-family: "Noto Serif", serif; font-style: italic; font-size: 25px; color: var(--footer-text); }
  .footer-text { position: absolute; font-size: 15.5px; line-height: 25px; color: var(--footer-text); }
  .community { position: absolute; left: 769px; top: 147px; display: flex; gap: 13px; }
  .community span { width: 34px; height: 34px; border-radius: 4px; background: rgba(255,255,255,.85); }
  .copyright {
    position: absolute; left: 0; top: 1157px; width: 1123px; height: 43px;
    background: var(--copyright-bg); text-align: center;
    font-size: 15px; line-height: 43px; color: #444;
  }
</style>
</head>
<body>
  <div class="top-band"></div>

  <div class="page">
    <div class="brand"><span class="brand-mark"></span>PELMO</div>

    <div class="lang">English</div>
    <span class="top-social" style="left:967px;background:#8fc9e8" role="img" aria-label="Social profile"></span>
    <span class="top-social" style="left:1001px;background:#5a6f9e" role="img" aria-label="Social profile"></span>

    <nav class="nav">
      <a href="#">HOME</a>
      <a href="#" class="active">PRODUCTS</a>
      <a href="#">NEWS</a>
      <a href="#">CONTACT</a>
    </nav>
    <div class="header-rule"></div>

    <div class="hero" role="img" aria-label="Photo of an excavator on a green worksite with crew in safety vests"></div>

    <h1 class="section-title">Products</h1>

    <a class="product-card left" href="#">
      <div class="product-name"><span class="dot"></span>PELMO</div>
      <div class="product-caption">Pelmo - WEB based Worksite Data Management service</div>
      <svg class="chevron" width="38" height="72" viewBox="0 0 38 72"><polyline points="2,2 36,36 2,70" fill="none" stroke="#b9b9b9" stroke-width="2"/></svg>
    </a>

    <a class="product-card right" href="#">
      <div class="product-name small">MAASTOPALAUTE</div>
      <div class="product-caption" style="left:32px">Maastopalaute</div>
      <svg class="chevron" width="38" height="72" viewBox="0 0 38 72"><polyline points="2,2 36,36 2,70" fill="none" stroke="#b9b9b9" stroke-width="2"/></svg>
    </a>
  </div>

  <footer class="footer">
    <div class="footer-label" style="left:38px;top:30px">EMAIL</div>
    <div class="footer-big" style="left:40px;top:55px">aarni.lehtola@varvikworks.com</div>
    <div class="footer-label" style="left:38px;top:120px">PHONE</div>
    <div class="footer-big" style="left:31px;top:143px">+358 40 712 0398</div>

    <div class="footer-label" style="left:769px;top:30px">CONTACT US</div>
    <div class="footer-text" style="left:769px;top:56px">Varvik Works<br>Pajatie 9, 00510 Helsinki</div>
    <div class="footer-label" style="left:769px;top:120px">COMMUNITY</div>
    <div class="community">
      <span role="img" aria-label="Social profile"></span>
      <span role="img" aria-label="Social profile"></span>
      <span role="img" aria-label="Social profile"></span>
      <span role="img" aria-label="Social profile"></span>
    </div>
  </footer>

  <div class="copyright">Copyright © 2012 Pelmo.</div>
</body>
</html>
```